Tall ridge firewood

It a new firewood outlet in Jindabyne nsw that will only sell top hardwood firewood (ironbark , red gum, grey gum, an box mix. I would like to see a web page the we can do order online payment for delivery. It will all so need to have photos of the firewood. I all so have logo for tall ridge firewood
Must have a modem look but easy to use I would like to see a black back ground of some sort.

Here are some other firewood web pages for ideas and firewood info
http://www.kestrelfirewood.example.au
http://www.dunmorefirewood.example.au
http://www.wrenlogfirewood.example.au
http://www.tallisbluelogs.example.au/firewood

```html
<!DOCTYPE html>
<html lang="en">
<head>
<meta charset="utf-8">
<title>Tall Ridge Firewood</title>
<link href="https://fonts.googleapis.com/css2?family=Open+Sans:ital,wght@0,400;0,600;0,700;1,700&family=Arimo:wght@400;700&display=swap" rel="stylesheet">
<style>
:root{
  --navy:#2c3e55;
  --ink:#3a4450;
  --muted:#6b7480;
  --blue:#4aa8e8;
  --blue-dark:#2d5f8f;
  --call-blue:#2a95d8;
  --footer:#2e3d4f;
  --footer-deep:#252f3c;
  --grey-band:#f5f5f5;
  --hero-dark:#1c120c;
  --pickup:#f3dd00;
  --zone1:#13a55a;
  --zone2:#0ea09a;
  --zone3:#e8622a;
  --zone4:#bf1a2f;
  --green-btn:#6cc417;
}
*{margin:0;padding:0;box-sizing:border-box}
html,body{width:1200px;height:2201px;overflow:hidden}
body{
  position:relative;
  font-family:"Open Sans",sans-serif;
  color:var(--ink);
  background:#2a120a;
}
.woodpile{
  position:absolute;left:0;top:0;width:1200px;height:1974px;
  background:
    radial-gradient(circle at 20% 15%,#6e2a14 0,transparent 120px),
    radial-gradient(circle at 85% 30%,#5c2210 0,transparent 140px),
    radial-gradient(circle at 10% 60%,#62250f 0,transparent 150px),
    radial-gradient(circle at 92% 75%,#6a2812 0,transparent 150px),
    linear-gradient(180deg,#3a170b,#2a0f07);
}
.page{position:absolute;left:189px;top:0;width:820px;height:1974px;background:#fff}

/* header */
.site-header{position:absolute;left:0;top:0;width:820px;height:165px;background:#fff}
.brand{position:absolute;left:36px;top:18px;display:flex;flex-direction:column;align-items:center;width:150px}
.brand-mark{width:70px;height:70px;border-radius:50%;background:var(--navy)}
.brand-name{margin-top:10px;font-weight:700;font-size:14px;color:var(--blue-dark);letter-spacing:.3px;white-space:nowrap}
.call-bar{position:absolute;left:447px;top:27px;height:38px;display:flex}
.call-bar .call{position:relative;background:var(--call-blue);color:#fff;font-size:14px;font-weight:600;line-height:38px;padding:0 24px 0 22px;z-index:1}
.call-bar .call::after{content:"";position:absolute;right:-16px;top:0;border-left:16px solid var(--call-blue);border-top:19px solid transparent;border-bottom:19px solid transparent}
.call-bar .avail{background:#e2e2e2;color:#2a7dbf;font-size:13.5px;line-height:38px;padding:0 10px 0 26px;width:200px}
.main-nav{position:absolute;top:98px;left:0;width:820px;font-size:15px;color:#4a4f55}
.main-nav a{position:absolute;color:inherit;text-decoration:none}
.main-nav a.active{color:var(--navy)}
.main-nav a.active::after{content:"";position:absolute;left:-4px;right:-4px;bottom:-6px;height:3px;background:var(--call-blue)}

/* hero */
.hero{position:absolute;left:0;top:165px;width:820px;height:450px;
  background:radial-gradient(ellipse at 35% 30%,#5a3e2a 0,#2c1c12 45%,var(--hero-dark) 100%);overflow:hidden}
.hero-logs{position:absolute;left:14px;top:70px;width:380px;height:200px;border-radius:30px;
  background:linear-gradient(135deg,#e2b070,#b87438 55%,#8a4c20)}
.hero-copy{position:absolute;left:451px;top:98px;width:340px;color:#fff}
.hero-copy h1{font-size:25px;font-weight:600;margin-bottom:16px}
.hero-copy p{font-size:14.5px;line-height:24px;color:#e8e4df}
.hero-actions{position:absolute;left:452px;top:256px;display:flex;align-items:center}
.btn{display:inline-block;font-size:14.5px;color:#fff;text-align:center;line-height:44px;text-decoration:none}
.btn-order{background:var(--blue-dark);width:136px}
.btn-more{background:var(--blue);width:136px}
.or{width:22px;height:22px;border-radius:50%;background:#1b2a3a;color:#fff;font-size:11px;line-height:20px;text-align:center;border:1px solid #fff;margin:0 -6px;position:relative;z-index:1}
.hero-wave{position:absolute;left:0;bottom:0;width:820px;height:80px}

/* intro */
.intro{position:absolute;left:0;top:614px;width:820px;height:370px}
.intro h2{position:absolute;left:28px;top:76px;font-size:19px;font-weight:400;color:#222}
.intro .copy{position:absolute;left:28px;top:114px;width:396px;font-size:13.6px;line-height:20.5px;color:#3c4a5c}
.intro .copy p+p{margin-top:20px}
.intro-photo{position:absolute;left:488px;top:81px;width:301px;height:225px;
  background:radial-gradient(ellipse at 45% 60%,#e04a1a 0,#7a1e08 30%,#1c1a1a 60%,#8c8780 100%)}

/* why */
.why{position:absolute;left:0;top:983px;width:820px;height:346px;background:var(--grey-band)}
.why h2{position:absolute;left:0;width:820px;top:38px;text-align:center;font-size:28px;font-weight:700;color:var(--navy)}
.feature{position:absolute;top:130px;width:220px;text-align:center}
.feature svg{display:block;margin:0 auto;height:90px}
.feature h3{margin-top:14px;font-size:15.5px;font-weight:400;color:#333}
.feature p{margin-top:10px;font-size:11.5px;line-height:16px;color:#555}

/* prices */
.prices{position:absolute;left:0;top:1329px;width:820px;height:645px}
.prices h2{position:absolute;left:0;width:820px;top:58px;text-align:center;font-size:24px;line-height:39px;font-weight:600;color:#111}
.rate-table{position:absolute;left:69px;top:170px;border-collapse:separate;border-spacing:2px;font-family:Arimo,sans-serif}
.rate-table th,.rate-table td{height:51px;text-align:center;vertical-align:middle}
.rate-table thead th{background:linear-gradient(#f8f8f8,#dcdcdc);font-size:21px;color:#222;width:76px}
.rate-table thead th.delivery{font-size:11px;line-height:13px;width:82px;font-weight:700}
.rate-table thead th.blank{background:none;width:106px}
.rate-table th.zone{font-size:18px;color:#fff;border-radius:6px 0 0 6px}
.rate-table td.fee{font-size:21px;font-weight:700;color:#fff}
.rate-table td.price{font-size:21px;font-weight:700;color:#1a1a1a}
.rate-table td.price span{font-size:10px;color:#999;font-weight:400;margin-right:4px;vertical-align:middle}
.row-pickup th.zone{background:var(--pickup);color:#111}
.row-pickup td.fee{background:#e7d63a;color:#b7a500}
.row-pickup td.price{background:#e8ddd0}
.row-z1 th.zone,.row-z1 td.fee{background:var(--zone1)}
.row-z1 td.price{background:#cde6d8}
.row-z2 th.zone,.row-z2 td.fee{background:var(--zone2)}
.row-z2 td.price{background:#c4e2df}
.row-z3 th.zone,.row-z3 td.fee{background:var(--zone3)}
.row-z3 td.price{background:#f1d5c7}
.row-z4 th.zone,.row-z4 td.fee{background:var(--zone4)}
.row-z4 td.price{background:#eccdd0}
.delivery-line{position:absolute;left:165px;top:500px;display:flex;align-items:center;font-size:15px;color:#333}
.delivery-line b{font-weight:700;margin-right:4px}
.delivery-line .or-text{margin:0 34px 0 24px}
.btn-online{background:linear-gradient(#8ee02e,#5aae10);color:#fff;font-weight:700;font-size:15px;width:176px;line-height:32px;border-radius:16px;text-align:center}

/* footer */
.site-footer{position:absolute;left:0;top:1974px;width:1200px;height:179px;background:var(--footer);color:#c9d2dc}
.footer-notch{position:absolute;left:565px;top:-17px;width:0;height:0;border-left:12px solid transparent;border-right:12px solid transparent;border-bottom:17px solid var(--footer)}
.footer-about{position:absolute;left:232px;top:20px;width:190px}
.footer-about h4{font-size:22px;font-weight:700;font-style:italic;color:#fff}
.footer-about p{margin-top:8px;font-size:9px;line-height:13.5px;color:#8b98a8}
.footer-contact{position:absolute;left:531px;top:22px}
.footer h5,.site-footer h5{font-size:14px;font-weight:400;color:#fff;margin-bottom:14px}
.contact-list{list-style:none;font-size:9.5px;line-height:13px;color:#c9d2dc}
.contact-list li{display:flex;gap:10px;margin-bottom:9px}
.contact-list svg{width:9px;height:10px;flex:none;margin-top:1px}
.footer-news{position:absolute;left:789px;top:22px;width:170px}
.footer-news p{font-size:9px;line-height:13px;color:#8b98a8}
.news-form{margin-top:14px;display:flex}
.news-form .field{width:130px;height:22px;background:#263342;font-size:9px;color:#6f7c8c;line-height:22px;padding-left:6px}
.news-form .send{width:35px;height:22px;background:var(--call-blue);display:flex;align-items:center;justify-content:center}
.copyright{position:absolute;left:0;top:2153px;width:1200px;height:48px;background:var(--footer-deep);text-align:center;line-height:48px;font-size:10px;color:#7c8896}
.copyright span{color:var(--call-blue)}
</style>
</head>
<body>
<div class="woodpile" role="img" aria-label="Stacked split firewood log ends in deep red-brown tones"></div>

<div class="page">
  <header class="site-header">
    <div class="brand">
      <div class="brand-mark"></div>
      <div class="brand-name">TALL RIDGE FIREWOOD</div>
    </div>
    <div class="call-bar">
      <div class="call">Call : 664-555-018</div>
      <div class="avail">Representatives Avaiable 24/7</div>
    </div>
    <nav class="main-nav">
      <a class="active" style="left:272px">Home</a>
      <a style="left:353px">Order Online</a>
      <a style="left:482px">About us</a>
      <a style="left:583px">Pricing</a>
      <a style="left:671px">FAQ</a>
      <a style="left:739px">Contact</a>
    </nav>
  </header>

  <section class="hero">
    <div class="hero-logs" role="img" aria-label="Split hardwood firewood logs"></div>
    <div class="hero-copy">
      <h1>Tall Ridge Firewood Store</h1>
      <p>These timbers are the slowest growing and the hardest of all hardwoods. Seasoned standing, dead, from 30 – 100 years.</p>
    </div>
    <div class="hero-actions">
      <a class="btn btn-order">Order Now</a>
      <span class="or">or</span>
      <a class="btn btn-more">Learn more</a>
    </div>
    <svg class="hero-wave" viewBox="0 0 820 80" preserveAspectRatio="none" aria-hidden="true">
      <path d="M0 70 C180 20 330 10 500 40 C640 62 740 55 820 20 L820 80 L0 80 Z" fill="#fff"/>
    </svg>
  </section>

  <section class="intro">
    <h2>Delivering Quality Firewood To Everyone</h2>
    <div class="copy">
      <p>Firewood is available all year round.The wood We supply is one of the best burning woods. This timber is suited to combustion &amp; open fireplaces. Our wood is premium quality and well seasoned. Guaranteed!</p>
      <p>Our wood is ECO friendly and only sourced from reputable suppliers, as we are a member of the Hardwood Suppliers Guild of Australia. We also supply a number of wood fired pizza shops and cafes with wood fire pizza ovens and heating for dining areas.</p>
    </div>
    <div class="intro-photo" role="img" aria-label="Wood heater with a glowing fire behind glass set in a stone hearth"></div>
  </section>

  <section class="why">
    <h2>Why Choose Tall Ridge Firewood?</h2>
    <div class="feature" style="left:23px">
      <svg viewBox="0 0 80 90" aria-hidden="true"><path d="M40 4 C46 22 64 30 66 56 C68 74 56 84 40 84 L14 84 C14 60 22 52 28 40 C32 52 36 54 38 52 C36 36 32 20 40 4 Z" fill="var(--navy)"/><rect x="6" y="80" width="68" height="6" fill="var(--navy)"/></svg>
      <h3>Long Burning</h3>
      <p>Harder to start but will burn 6 – 8 hours. These timbers are the slowest growing and the hardest of all hardwoods.</p>
    </div>
    <div class="feature" style="left:313px">
      <svg viewBox="0 0 80 90" aria-hidden="true"><rect x="33" y="4" width="14" height="8" fill="var(--navy)"/><circle cx="40" cy="50" r="32" fill="none" stroke="var(--navy)" stroke-width="7"/><path d="M40 50 L56 60" stroke="var(--navy)" stroke-width="5" stroke-linecap="round"/></svg>
      <h3>Very Little Ash</h3>
      <p>Clean out fire only once per season approximately.</p>
    </div>
    <div class="feature" style="left:578px">
      <svg viewBox="0 0 110 90" aria-hidden="true" style="height:60px;margin-top:30px"><g fill="var(--navy)"><rect x="0" y="42" width="110" height="5"/><rect x="14" y="22" width="10" height="45"/><rect x="28" y="28" width="8" height="33"/><rect x="86" y="22" width="10" height="45"/><rect x="74" y="28" width="8" height="33"/><rect x="50" y="34" width="10" height="21"/></g></svg>
      <h3>Strong Burning</h3>
      <p>Cannot be put out even if the vent closed, unless water is used.</p>
    </div>
  </section>

  <section class="prices">
    <h2>We sell Premium Seasoned Firewood and it is<br>sold for delivery at the following rates:</h2>
    <table class="rate-table">
      <thead>
        <tr><th class="blank"></th><th class="delivery">Delivery<br>Charged</th><th>1m³</th><th>2m³</th><th>3m³</th><th>4m³</th><th>5m³</th><th>6m³</th></tr>
      </thead>
      <tbody>
        <tr class="row-pickup"><th class="zone">Pick up</th><td class="fee">X</td><td class="price"><span>$</span>210</td><td class="price"><span>$</span>410</td><td class="price"><span>$</span>590</td><td class="price"><span>$</span>750</td><td class="price"><span>$</span>890</td><td class="price"><span>$</span>1010</td></tr>
        <tr class="row-z1"><th class="zone">ZONE 01</th><td class="fee">Free</td><td class="price"><span>$</span>220</td><td class="price"><span>$</span>420</td><td class="price"><span>$</span>600</td><td class="price"><span>$</span>760</td><td class="price"><span>$</span>900</td><td class="price"><span>$</span>1020</td></tr>
        <tr class="row-z2"><th class="zone">ZONE 02</th><td class="fee">$45</td><td class="price"><span>$</span>265</td><td class="price"><span>$</span>465</td><td class="price"><span>$</span>645</td><td class="price"><span>$</span>805</td><td class="price"><span>$</span>945</td><td class="price"><span>$</span>1065</td></tr>
        <tr class="row-z3"><th class="zone">ZONE 03</th><td class="fee">$65</td><td class="price"><span>$</span>285</td><td class="price"><span>$</span>485</td><td class="price"><span>$</span>665</td><td class="price"><span>$</span>825</td><td class="price"><span>$</span>965</td><td class="price"><span>$</span>1085</td></tr>
        <tr class="row-z4"><th class="zone">ZONE 04</th><td class="fee">$85</td><td class="price"><span>$</span>310</td><td class="price"><span>$</span>505</td><td class="price"><span>$</span>685</td><td class="price"><span>$</span>845</td><td class="price"><span>$</span>985</td><td class="price"><span>$</span>1105</td></tr>
      </tbody>
    </table>
    <div class="delivery-line">
      <b>Delivery :</b> Phone us on :(02) 5550 1842
      <span class="or-text">or</span>
      <a class="btn-online">Order Online</a>
    </div>
  </section>
</div>

<footer class="site-footer">
  <div class="footer-notch"></div>
  <div class="footer-about">
    <h4>TallRidge</h4>
    <p>Seasoned hardwood split and stacked for winter, delivered across the Snowy Mountains region by a small local team.</p>
  </div>
  <div class="footer-contact">
    <h5>CONTACT</h5>
    <ul class="contact-list">
      <li><svg viewBox="0 0 10 12"><path d="M5 0 C2 0 0 2 0 4.5 C0 8 5 12 5 12 C5 12 10 8 10 4.5 C10 2 8 0 5 0 Z" fill="var(--blue)"/><circle cx="5" cy="4.5" r="1.6" fill="var(--footer)"/></svg><span>4567 Street name,<br>012 12 City name, Country</span></li>
      <li><svg viewBox="0 0 10 12"><path d="M2 0 L4 3 L3 5 C4 7 5 8 6 9 L8 8 L10 10 L8 12 C3 11 0 6 0 2 Z" fill="var(--blue)"/></svg><span>+012 3456 789</span></li>
      <li><svg viewBox="0 0 10 10"><rect x="0" y="2" width="10" height="7" fill="var(--blue)"/><path d="M0 2 L5 6 L10 2" stroke="var(--footer)" fill="none"/></svg><span>email@domain.com</span></li>
      <li><svg viewBox="0 0 10 10"><circle cx="5" cy="5" r="4.5" fill="none" stroke="var(--blue)"/><path d="M0.5 5 H9.5 M5 0.5 V9.5" stroke="var(--blue)"/></svg><span>www.example-site.com</span></li>
    </ul>
  </div>
  <div class="footer-news">
    <h5>NEWSLETTER</h5>
    <p>Sign up for seasonal prices, delivery days and winter stock updates from our yard.</p>
    <div class="news-form">
      <div class="field">email address</div>
      <div class="send"><svg width="12" height="10" viewBox="0 0 12 10"><path d="M0 3 H6 V0 L12 5 L6 10 V7 H0 Z" fill="#fff"/></svg></div>
    </div>
  </div>
</footer>
<div class="copyright"><span>TallRidgeFirewood</span> Copyright 2013 | All rights reserved.</div>
</body>
</html>
```